Bold Cover needed for a book on Workplace Bullying

I need a book cover design for a book titled, “Quiet Harbour?” The book recounts my story of bullying in the workplace. It also includes chapters on how readers can minimize/stop workplace bullying, write an effective complaint, and ensure their own mental wellbeing.
I am looking for a bold design using red and black, and possibly distressed lettering. The covers of other books dealing with this subject do not reflect my vision. They are often too childish or look too academic. This book needs to stress the serious nature of a toxic workplace, while appealing to readers experiencing a similar situation. I’d like the cover to reflect the mental anguish associated with workplace bullying (hence the distressed lettering).
I have included a cover that appeals to me (although the coloring is wrong). That said, I am also very happy (and excited) to see your creative input!
On the cover, it should have the following:
Title: Quiet Harbour?
Subtitle: How the Transit Department Condones Bullying & Ruins Lives
Author: Owen Petrick
Other relevant details:
Book size: 5.5” x 8.5”
Back cover will have a blurb, author picture/short bio, and barcode
The blurb on the back cover reads:
Undermining, intimidation and threats
Despite the Department of Transit allegedly holding a zero tolerance for bullying, these behaviours were an everyday occurrence in at least one workplace. Even after a decade of complaints, numerous witnesses and physical proof, the department failed to act. Instead, they looked the other way, allowing one powerful and well-connected individual to end careers and ruin lives.
After being targeted, one teacher resolved to put an end to the abuse experienced by more than fifty employees. His startling story reveals the relentless bullying, mental health ramifications, and insidious tactics used to cover up the corrosive behaviour.
Those who have experienced a toxic workplace will also find much needed support and guidance, intended to minimise suffering and detail a clear way forward. Chapters include dealing with bullying in the workplace, how to lodge a successful complaint, and how to stay sane during any potential legal action.

```html
<!DOCTYPE html>
<html lang="en">
<head>
<meta charset="utf-8">
<title>Quiet Harbour? — Book Cover Wrap</title>
<link rel="stylesheet" href="https://fonts.googleapis.com/css2?family=Open+Sans:wght@600;700&family=Playfair+Display&family=Great+Vibes&family=Rubik+Dirt&display=swap">
<style>
  :root {
    --stage: #2a2a2a;
    --ink: #070707;
    --red: #ee1c1c;
    --red-deep: #e81818;
    --wrap-w: 1110px;
    --wrap-h: 784px;
  }
  * { box-sizing: border-box; margin: 0; padding: 0; }
  html, body {
    width: 1200px; height: 960px; overflow: hidden;
    background: var(--stage);
  }
  .wrap {
    position: absolute; left: 45px; top: 88px;
    width: var(--wrap-w); height: var(--wrap-h);
    display: flex;
  }

  /* Back cover */
  .back-cover {
    width: 512px; height: 100%;
    background: var(--ink);
    color: var(--red);
    position: relative;
  }
  .back-heading {
    position: absolute; top: 22px; left: 0; right: 0;
    text-align: center;
    font-family: "Great Vibes", cursive;
    font-size: 72px; font-weight: 400;
    line-height: 1;
  }
  .blurb {
    position: absolute; left: 72px; width: 380px;
    font-family: "Playfair Display", serif;
    font-size: 15.6px; line-height: 19.4px;
    text-align: center;
  }
  .blurb-1 { top: 145px; }
  .blurb-2 { top: 320px; }
  .blurb-3 { top: 456px; }
  .blurb-4 { top: 670px; }

  /* Spine */
  .spine {
    width: 86px; height: 100%;
    background: var(--ink);
    border-left: 1px solid #151515;
    border-right: 1px solid #151515;
    position: relative;
  }
  .spine-author {
    position: absolute; left: 50%; top: 386px;
    transform: translate(-50%, -50%) rotate(-90deg);
    white-space: nowrap;
    font-family: "Playfair Display", serif;
    font-size: 31px; letter-spacing: 1px;
    color: var(--red);
  }

  /* Front cover */
  .front-cover {
    width: 512px; height: 100%;
    background: var(--red);
    position: relative; overflow: hidden;
  }
  .dark-field {
    position: absolute; left: 253px; top: 364px; right: 0; bottom: 0;
    background: var(--ink);
  }
  .profile {
    position: absolute; background: var(--ink);
  }
  .profile-left {
    left: 0; top: 410px; width: 68px; height: 308px;
    border-radius: 0 60px 30px 0;
  }
  .profile-right {
    left: 186px; top: 424px; width: 80px; height: 302px;
    border-radius: 60px 0 0 30px;
  }
  .title { font-weight: 700; }
  .title-initial {
    position: absolute; left: 8px; top: -62px;
    font-family: "Open Sans", sans-serif;
    font-size: 470px; line-height: 1;
    color: var(--ink);
    transform: scaleX(0.74); transform-origin: left top;
  }
  .title-rest {
    position: absolute; left: 270px; top: 232px;
    font-family: "Open Sans", sans-serif;
    font-size: 108px; line-height: 1; letter-spacing: -3px;
    color: var(--ink);
  }
  .title-second {
    position: absolute; left: 451px; top: 542px;
    transform: translate(-50%, -50%) rotate(90deg);
    white-space: nowrap;
    font-family: "Rubik Dirt", sans-serif;
    font-size: 60px; line-height: 1; font-weight: 400; letter-spacing: 2px;
    color: var(--red);
  }
  .title-mark {
    position: absolute; left: 270px; top: 409px;
    font-family: "Rubik Dirt", sans-serif;
    font-size: 220px; line-height: 1; font-weight: 400;
    color: var(--red-deep);
    transform: scaleY(1.45); transform-origin: left top;
  }
  .subtitle {
    position: absolute; left: 0; right: 0; top: 730px;
    font-family: "Open Sans", sans-serif;
    font-weight: 600; font-size: 21.5px; line-height: 23px;
    text-align: center; text-transform: uppercase;
    padding-left: 26px; padding-right: 0;
    white-space: nowrap;
  }
  .subtitle-on-red { color: var(--ink); clip-path: inset(0 259px 0 0); }
  .subtitle-on-dark { color: var(--red); clip-path: inset(0 0 0 253px); }
</style>
</head>
<body>
  <div class="wrap">
    <section class="back-cover">
      <h2 class="back-heading">Free</h2>
      <p class="blurb blurb-1">Lorem ipsum dolor sit amet, consectetur adipiscing elit, sed do eiusmod tempor incididunt ut labore et dolore magna aliqua. Quis ipsum suspendisse ultrices gravida. Risus commodo viverra maecenas accumsan lacus vel facilisis. Lore incididunt ut labore et dolore magna aliqua. Quis ipsum suspendisse ultrices gravida. Risus commodo viverra maecenas accumsan lacus vel facilisis.</p>
      <p class="blurb blurb-2">Lorem ipsum dolor sit amet, consectetur adipiscing elit, sed do eiusmod tempor incididunt ut labore et dolore magna aliqua. Quis ipsum suspendisse ultrices gravida. Risus commodo viverra maecenas accumsan lacus vel facilisis.</p>
      <p class="blurb blurb-3">Lorem ipsum dolor sit amet, consectetur adipiscing elit, sed do eiusmod tempor incididunt ut labore et dolore magna aliqua. Quis ipsum suspendisse ultrices gravida. Risus commodo viverra maecenas accumsan lacus vel facilisis. Lorem ipsum dolor sit amet, consectetur adipiscing elit, sed do eiusmod tempor incididunt ut labore et dolore magna aliqua. Quis ipsum suspendisse ultrices gravida. Risus commodo viverra maecenas accumsan lacus vel facilisis.</p>
      <p class="blurb blurb-4">Lorem ipsum dolor sit ae ultrices gravida. Risus commodo viverra maecenas accumsan lacus vel facilisis.</p>
    </section>

    <section class="spine">
      <span class="spine-author">OWEN PETRICK</span>
    </section>

    <section class="front-cover">
      <div class="dark-field"></div>
      <div class="profile profile-left" role="img" aria-label="Black silhouette of a head in profile facing right"></div>
      <div class="profile profile-right" role="img" aria-label="Black silhouette of a head in profile facing left"></div>
      <h1 class="title">
        <span class="title-initial">Q</span>
        <span class="title-rest">UIET</span>
        <span class="title-mark">?</span>
        <span class="title-second">HARBOUR</span>
      </h1>
      <p class="subtitle subtitle-on-red">How the Transit Department Condones<br>Bullying &amp; Ruins Lives</p>
      <p class="subtitle subtitle-on-dark" aria-hidden="true">How the Transit Department Condones<br>Bullying &amp; Ruins Lives</p>
    </section>
  </div>
</body>
</html>
```